Brisk Framing website

I need a website for my construction. I want customers to see past builds and current projects Something that stands out and reflects awareness, safety, attention to details. I already have a logo designed by Pixel Harbor
Target Market(s)
Residential and Commercial sectors
Industry/Entity Type
Construction
Logo Text
Brisk Framing
Colors
EB3D1F
EC4F4E
F09395
F8D3D4
FCEDEE
Requirements
Must have
- My contact info
Nice to have
- Past projects

```html
<!DOCTYPE html>
<html lang="en">
<head>
<meta charset="utf-8">
<title>Brisk Framing</title>
<link href="https://fonts.googleapis.com/css2?family=Roboto:wght@400;500;700;900&display=swap" rel="stylesheet">
<style>
:root{
  --red:#eb3d1f;
  --red-soft:#ec4f4e;
  --pink:#f09395;
  --blush:#f8d3d4;
  --tint:#eaf2f8;
  --ink:#1b1b1b;
  --body:#555;
  --footer:#111214;
  --white:#fff;
}
*{box-sizing:border-box;margin:0;padding:0}
html,body{width:1200px;height:5042px;overflow:hidden}
body{font-family:'Roboto',sans-serif;color:var(--ink);background:var(--white);position:relative}
.abs{position:absolute}
section,header,footer{position:absolute;left:0;width:1200px}
.heading{font-weight:700;font-size:37px;text-align:center;width:100%;position:absolute;left:0;letter-spacing:.3px}
.lead{font-size:14.5px;line-height:27px;color:var(--body);text-align:center;width:660px;left:270px;position:absolute}
.btn{position:absolute;background:var(--red);color:#fff;font-weight:700;font-size:14px;display:flex;align-items:center;justify-content:center;letter-spacing:.3px}

/* header */
.site-header{top:0;height:98px;background:#fff}
.brand{left:100px;top:18px;display:flex;align-items:center;gap:10px;color:var(--red);font-weight:900;font-size:28px;letter-spacing:.5px}
.brand .mark{width:18px;height:18px;background:var(--red)}
.topbar{left:342px;top:0;width:858px;height:38px;background:var(--red);clip-path:polygon(0 0,100% 0,100% 100%,24px 100%);color:#fff;font-size:11.5px;display:flex;align-items:center}
.topbar span{display:flex;align-items:center;gap:7px;position:absolute}
.topbar svg{fill:#fff}
.nav a{position:absolute;top:62px;font-size:14.5px;font-weight:700;color:var(--ink);text-decoration:none}
.nav .active{color:var(--red)}
.quote-outline{left:943px;top:51px;width:155px;height:39px;border:2px solid var(--red);color:var(--red);font-weight:700;font-size:14px;display:flex;align-items:center;justify-content:center}

/* hero */
.hero{top:98px;height:597px;background:linear-gradient(180deg,#7f9aa8 0%,#a9a59a 35%,#8a5a3a 65%,#5a2f1c 100%)}
.hero h1{left:100px;top:215px;color:#fff;font-size:40px;font-weight:700;position:absolute}
.hero p{left:100px;top:275px;width:430px;color:#fff;font-size:16px;line-height:27px;position:absolute}
.hero .chev{top:300px;width:22px;height:22px;border-left:2px solid #fff;border-bottom:2px solid #fff;position:absolute;opacity:.8}
.dots{left:560px;top:568px;display:flex;gap:10px;position:absolute}
.dots i{width:12px;height:12px;border:2px solid #fff;border-radius:50%}
.dots i.on{background:#fff}

/* about */
.about{top:695px;height:542px}
.about .photo{left:100px;top:92px;width:415px;height:319px;background:linear-gradient(160deg,#b9d3e6,#c08a55 60%,#6b4326)}
.since{left:386px;top:288px;width:158px;height:154px;background:var(--red);color:#fff;text-align:center;border:2px solid #fff}
.since small{display:block;margin-top:38px;font-size:14px;font-weight:700}
.since b{display:block;font-size:44px;font-weight:500;margin-top:2px}
.about h2{left:617px;top:103px;font-size:37px;font-weight:700;position:absolute}
.about h3{left:617px;top:151px;font-size:27px;font-weight:700;position:absolute}
.about .copy{left:617px;top:198px;width:480px;font-size:14px;line-height:26px;color:#444;position:absolute}
.about .copy p+p{margin-top:9px}
.phone-line{left:832px;top:393px;font-size:20px;font-weight:700;display:flex;align-items:center;gap:10px;position:absolute}

/* services */
.services{top:1237px;height:560px;background:var(--tint)}
.service-card{top:186px;width:240px;height:311px;position:absolute;color:#fff}
.service-card .icon{position:absolute;left:96px;top:198px;width:48px;height:48px;border-radius:50%;background:var(--red);border:2px solid #fff}
.service-card .name{position:absolute;left:0;width:100%;text-align:center;bottom:22px;font-weight:700;font-size:16px}
.service-card.featured{background:var(--red)}
.service-card.featured .icon{top:34px;background:none;border:2px solid #fff}
.service-card.featured .name{top:96px;bottom:auto}
.service-card.featured p{position:absolute;top:128px;left:20px;width:200px;font-size:11px;line-height:21px;text-align:center}

/* gallery */
.gallery{top:1797px;height:1055px}
.tile{position:absolute}

/* clients */
.clients{top:2852px;height:559px;background:var(--tint)}
.review{position:absolute;top:219px;width:456px;height:256px;background:#fff;padding:26px 26px}
.review h4{font-size:16.5px;font-weight:700}
.review p{margin-top:14px;font-size:12px;line-height:23px;color:#555}
.reviewer{margin-top:12px;display:flex;align-items:center;gap:10px;font-size:13px}
.reviewer i{width:34px;height:34px;border-radius:50%;background:#c9c2bb}
.review .q{position:absolute;right:18px;bottom:-14px;font-size:90px;color:#ddd;font-weight:700;line-height:1}
.arrow{position:absolute;top:3190px}

/* news */
.news{top:3411px;height:722px}
.post{position:absolute;top:223px;width:320px;height:401px;background:#fff;box-shadow:0 2px 14px rgba(0,0,0,.1)}
.post .img{position:absolute;left:8px;top:10px;width:304px;height:206px}
.post .date{position:absolute;left:92px;top:194px;width:136px;height:26px;background:var(--red);color:#fff;font-size:12.5px;display:flex;align-items:center;justify-content:center;gap:6px}
.post h5{position:absolute;left:10px;top:240px;width:300px;font-size:16.5px;font-weight:700;line-height:21px}
.post p{position:absolute;left:10px;top:290px;width:300px;font-size:11.5px;line-height:21px;color:#666}
.post .more{position:absolute;left:10px;top:362px;font-size:12px;font-weight:700}

/* contact */
.contact{top:4133px;height:501px;background:var(--red)}
.contact .scene{left:691px;top:0;width:509px;height:501px;background:linear-gradient(170deg,#8a9db0,#c9a46a 55%,#6b5a44)}
.contact h2{left:100px;top:108px;color:#fff;font-size:37px;font-weight:500;position:absolute;display:flex;align-items:center;gap:10px}
.contact h2::after{content:"";width:30px;height:2px;background:#fff}
.field{position:absolute;background:#fff;font-size:12px;padding:10px 12px;color:#333}
.submit{left:100px;top:372px;width:151px;height:38px;border:2px solid #fff;color:#fff;font-weight:700;font-size:13px;display:flex;align-items:center;justify-content:center;position:absolute}

/* footer */
.site-footer{top:4634px;height:408px;background:var(--footer);color:#fff}
.foot-brand{left:100px;top:116px;font-size:28px;font-weight:900;letter-spacing:.5px;position:absolute}
.social{left:122px;top:214px;display:flex;gap:8px;position:absolute}
.social i{width:36px;height:36px;border:1.5px solid #fff;border-radius:50%}
.col{position:absolute;top:106px;font-size:13px}
.col h6{font-size:16.5px;font-weight:700;margin-bottom:18px}
.col li{list-style:none;line-height:28px}
.info{display:flex;gap:10px;line-height:20px;margin-bottom:12px}
.newsletter-input{left:816px;top:178px;width:282px;height:49px;background:#fff;border-radius:25px;color:#333;font-size:13px;padding:16px 22px;position:absolute}
.newsletter-go{left:1050px;top:178px;width:48px;height:49px;background:var(--red);border-radius:0 25px 25px 0;display:flex;align-items:center;justify-content:center;position:absolute}
.rule{left:92px;top:339px;width:1016px;height:1px;background:#444;position:absolute}
.copyright{top:364px;left:0;width:100%;text-align:center;font-size:13px;position:absolute}
</style>
</head>
<body>

<header class="site-header">
  <div class="brand abs"><span class="mark"></span>BRISK FRAMING</div>
  <div class="topbar abs">
    <span style="left:130px"><svg width="11" height="14" viewBox="0 0 12 16"><path d="M6 0a6 6 0 0 0-6 6c0 4.5 6 10 6 10s6-5.5 6-10a6 6 0 0 0-6-6zm0 8.5A2.5 2.5 0 1 1 6 3.5a2.5 2.5 0 0 1 0 5z"/></svg>Harbourside Avenue, ACT, Australia 2900</span>
    <span style="left:390px"><svg width="14" height="14" viewBox="0 0 16 16"><circle cx="8" cy="8" r="7" fill="none" stroke="#fff" stroke-width="1.6"/><path d="M8 4v4l3 2" stroke="#fff" stroke-width="1.6" fill="none"/></svg>MON - FRI 8am - 5pm</span>
    <span style="left:590px;font-size:18px;font-weight:500"><svg width="15" height="15" viewBox="0 0 24 24"><path d="M6.6 10.8a15 15 0 0 0 6.6 6.6l2.2-2.2a1 1 0 0 1 1-.25 11.4 11.4 0 0 0 3.6.57 1 1 0 0 1 1 1V20a1 1 0 0 1-1 1A17 17 0 0 1 3 4a1 1 0 0 1 1-1h3.5a1 1 0 0 1 1 1c0 1.25.2 2.45.57 3.57a1 1 0 0 1-.25 1z"/></svg>+204.555.0190</span>
  </div>
  <nav class="nav">
    <a class="active" style="left:427px">HOME</a>
    <a style="left:522px">SERVICES</a>
    <a style="left:644px">GALLERY</a>
    <a style="left:761px">FAQ</a>
    <a style="left:843px">CONTACT</a>
  </nav>
  <div class="quote-outline abs">GET A QUOTE</div>
</header>

<section class="hero" role="img" aria-label="Worker on a high-rise construction site with cranes and a city skyline at dusk">
  <i class="chev" style="left:66px;transform:rotate(45deg)"></i>
  <i class="chev" style="left:1118px;transform:rotate(-135deg)"></i>
  <h1>BRISK FRAMING</h1>
  <p>Lorem ipsum dolor sit amet, consectetur adipiscing elit, sed do eiusmod tempor incididunt ut labore</p>
  <div class="btn" style="left:100px;top:344px;width:192px;height:47px">GET A QUOTE</div>
  <div class="dots"><i></i><i class="on"></i><i></i><i></i></div>
</section>

<section class="about">
  <div class="photo abs" role="img" aria-label="Timber house frame under construction"></div>
  <div class="since abs"><small>SINCE</small><b>1970</b></div>
  <h2>ABOUT US</h2>
  <h3>RIDGELINE CONCRETING AND EXCAVATION</h3>
  <div class="copy">
    <p>Sed ut perspiciatis unde omnis iste natus error sit vtatem accusantium doloremque laudantium, totam rem aperiam, epsa quae a illo inventore veritatis et quasi architecto beatae vita</p>
    <p>Sed ut perspiciatis unde omnis iste natus error sit vtatem accusantium doloremque laudantium, totam rem aperiam, epsa quae ab illo inventore veritatis et quasi architecto beatae vita</p>
  </div>
  <div class="btn" style="left:617px;top:383px;width:191px;height:47px">LEARN MORE</div>
  <div class="phone-line"><svg width="20" height="20" viewBox="0 0 24 24"><path fill="#1b1b1b" d="M6.6 10.8a15 15 0 0 0 6.6 6.6l2.2-2.2a1 1 0 0 1 1-.25 11.4 11.4 0 0 0 3.6.57 1 1 0 0 1 1 1V20a1 1 0 0 1-1 1A17 17 0 0 1 3 4a1 1 0 0 1 1-1h3.5a1 1 0 0 1 1 1c0 1.25.2 2.45.57 3.57a1 1 0 0 1-.25 1z"/></svg>204.555.0190</div>
</section>

<section class="services">
  <h2 class="heading" style="top:54px">SERVICES WE PROVIDE</h2>
  <p class="lead" style="top:106px">Lorem ipsum dolor sit amet, consectetur adipiscing elit, sed do eiusmod tempor incididunt ut labore et dolore magna aliqua. Quis ipsum suspendisse ultrices gravida.</p>
  <div class="service-card" style="left:100px;background:linear-gradient(180deg,#8fbfe0,#8a8f96 60%,#4e5258)" role="img" aria-label="Steel frame building under construction"><span class="icon"></span><span class="name">FINIBUS BONORUM</span></div>
  <div class="service-card" style="left:354px;background:linear-gradient(180deg,#3f8fd6,#c7b8a3 60%,#6f6a62)" role="img" aria-label="Tower crane over concrete building"><span class="icon"></span><span class="name">FINIBUS BONORUM</span></div>
  <div class="service-card featured" style="left:607px"><span class="icon" style="left:96px"></span><span class="name">FINIBUS BONORUM</span><p>Sed ut perspiciatis omnis iste natus error sit voluptatem accusantium doloremque laudantium, totam aperiam, eaque ipsa quae ab illo inventore veritatis et quasi architecto beatae vitae dicnt explicabo. Nemo enim ipsam voluptatem</p></div>
  <div class="service-card" style="left:861px;background:linear-gradient(180deg,#a9c6de,#7c8a6a 55%,#5b4f3c)" role="img" aria-label="Drilling rig on an excavation site"><span class="icon"></span><span class="name">FINIBUS BONORUM</span></div>
</section>

<section class="gallery">
  <h2 class="heading" style="top:92px">OUR GALLERY</h2>
  <p class="lead" style="top:144px">Lorem ipsum dolor sit amet, consectetur adipiscing elit, sed do eiusmod tempor incididunt ut labore et dolore magna aliqua. Quis ipsum suspendisse ultrices gravida.</p>
  <div class="tile" style="left:100px;top:229px;width:661px;height:318px;background:linear-gradient(200deg,#b8d0e4,#5b7fa8 60%,#283c5e)" role="img" aria-label="Blue steel structure and crane against the sky"></div>
  <div class="tile" style="left:775px;top:229px;width:325px;height:318px;background:linear-gradient(180deg,#6fa7d8,#a9b3b8 60%,#6e6a62)" role="img" aria-label="Glass office tower under construction"></div>
  <div class="tile" style="left:100px;top:559px;width:325px;height:319px;background:linear-gradient(160deg,#7c8c96,#5f6e78 50%,#3c3a36)" role="img" aria-label="Aerial view of concrete floor plates and excavator"></div>
  <div class="tile" style="left:438px;top:559px;width:323px;height:319px;background:linear-gradient(190deg,#3a7cc4,#9db6cc 55%,#505860)" role="img" aria-label="High-rise facade under construction"></div>
  <div class="tile" style="left:775px;top:559px;width:325px;height:319px;background:linear-gradient(180deg,#d9d2c4,#b7a990 55%,#4e4336)" role="img" aria-label="Concrete building frame with tower crane"></div>
  <div class="btn" style="left:505px;top:913px;width:192px;height:47px">VIEW OUR WORK</div>
</section>

<section class="clients">
  <h2 class="heading" style="top:80px">OUR SATISFIED CLIENTS</h2>
  <p class="lead" style="top:132px">Lorem ipsum dolor sit amet, consectetur adipiscing elit, sed do eiusmod tempor incididunt ut labore et dolore magna aliqua. Quis ipsum suspendisse ultrices gravida.</p>
  <div class="review" style="left:131px">
    <h4>LANDSCAPE CONTRACTOR GRANTS PASS</h4>
    <p>We have used Stonebrook Excavate &amp; Fence for several projects on our property, and couldn't be happier. Marco is prompt in responding to calls and emails, creative, skilled and always friendly and professional. It feels great knowing that we can TRUST him to get each job done well—on time and on budget..</p>
    <div class="reviewer"><i role="img" aria-label="Client portrait"></i>Tom Harlow &amp; Nina Perez</div>
    <span class="q">”</span>
  </div>
  <div class="review" style="left:620px">
    <h4>EXCAVATION WORK JACKSONVILLE</h4>
    <p>Stonebrook Excavating just completed in early June, 2017 a small grading job on one of the primary logging roads on my property to add water bars and solve a drainage problem I was having. Marco and I discussed the water damage and how to remedy the problem months earlier. He came by during the rainy season.....</p>
    <div class="reviewer"><i role="img" aria-label="Client portrait"></i>Tom Harlow &amp; Nina Perez</div>
    <span class="q">”</span>
  </div>
  <svg class="abs" style="left:78px;top:338px" width="34" height="20" viewBox="0 0 34 20"><path d="M33 10H2M10 2 2 10l8 8" stroke="#333" stroke-width="2" fill="none"/></svg>
  <svg class="abs" style="left:1090px;top:338px" width="34" height="20" viewBox="0 0 34 20"><path d="M1 10h31M24 2l8 8-8 8" stroke="#333" stroke-width="2" fill="none"/></svg>
</section>

<section class="news">
  <h2 class="heading" style="top:88px">LATEST NEWS</h2>
  <p class="lead" style="top:140px">Lorem ipsum dolor sit amet, consectetur adipiscing elit, sed do eiusmod tempor incididunt ut labore et dolore magna aliqua. Quis ipsum suspendisse ultrices gravida.</p>

  <article class="post" style="left:100px">
    <div class="img" style="background:linear-gradient(160deg,#7c8c96,#4f5c64 55%,#2f2d2a)" role="img" aria-label="Aerial view of a building site"></div>
    <div class="date"><svg width="11" height="11" viewBox="0 0 12 12"><rect x="1" y="2" width="10" height="9" fill="none" stroke="#fff" stroke-width="1.4"/><path d="M1 5h10" stroke="#fff"/></svg>JUNE 04,2021</div>
    <h5>Section 1.10.32 of "de Finibus Bonor um et Malorum"</h5>
    <p>Sed ut perspiciatis unde omnis iste natus error sit voluptatem accusantium doloremque laudantium, totam rem aperiam</p>
    <span class="more">READ MORE ▸</span>
  </article>
  <article class="post" style="left:440px">
    <div class="img" style="background:linear-gradient(180deg,#3f8fd6,#b7c4cc 60%,#7a7468)" role="img" aria-label="Crane beside an apartment block"></div>
    <div class="date"><svg width="11" height="11" viewBox="0 0 12 12"><rect x="1" y="2" width="10" height="9" fill="none" stroke="#fff" stroke-width="1.4"/><path d="M1 5h10" stroke="#fff"/></svg>JUNE 04,2021</div>
    <h5>Section 1.10.32 of "de Finibus Bonor um et Malorum"</h5>
    <p>Sed ut perspiciatis unde omnis iste natus error sit voluptatem accusantium doloremque laudantium, totam rem aperiam</p>
    <span class="more">READ MORE ▸</span>
  </article>
  <article class="post" style="left:780px">
    <div class="img" style="background:linear-gradient(180deg,#c9c6c0,#a28a78 55%,#6b5446)" role="img" aria-label="Rebar deck on a rooftop site"></div>
    <div class="date"><svg width="11" height="11" viewBox="0 0 12 12"><rect x="1" y="2" width="10" height="9" fill="none" stroke="#fff" stroke-width="1.4"/><path d="M1 5h10" stroke="#fff"/></svg>JUNE 04,2021</div>
    <h5>Section 1.10.32 of "de Finibus Bonor um et Malorum"</h5>
    <p>Sed ut perspiciatis unde omnis iste natus error sit voluptatem accusantium doloremque laudantium, totam rem aperiam</p>
    <span class="more">READ MORE ▸</span>
  </article>
</section>

<section class="contact">
  <div class="scene abs" role="img" aria-label="Three site engineers in hard hats reviewing plans"></div>
  <h2>GET IN TOUCH</h2>
  <div class="field" style="left:100px;top:169px;width:229px;height:41px">First Name:</div>
  <div class="field" style="left:344px;top:169px;width:229px;height:41px">Last Name:</div>
  <div class="field" style="left:100px;top:225px;width:229px;height:39px">Email:</div>
  <div class="field" style="left:344px;top:225px;width:229px;height:39px">Phone:</div>
  <div class="field" style="left:100px;top:282px;width:473px;height:76px">Message:</div>
  <div class="submit">SUBMIT NOW</div>
</section>

<footer class="site-footer">
  <div class="foot-brand">BRISK FRAMING</div>
  <div class="social"><i></i><i></i><i></i><i></i></div>
  <div class="col" style="left:391px">
    <h6>QUICK LINK</h6>
    <ul><li>Home</li><li>Services</li><li>Gallery</li><li>Online quote</li><li>FAQ</li><li>Contact</li></ul>
  </div>
  <div class="col" style="left:566px;width:220px">
    <h6>CONTACT US</h6>
    <div class="info"><svg width="12" height="16" viewBox="0 0 12 16"><path fill="#fff" d="M6 0a6 6 0 0 0-6 6c0 4.5 6 10 6 10s6-5.5 6-10a6 6 0 0 0-6-6zm0 8.5A2.5 2.5 0 1 1 6 3.5a2.5 2.5 0 0 1 0 5z"/></svg><span>123 Your Adress Goes Here.<br>CA, 1234567</span></div>
    <div class="info"><svg width="14" height="12" viewBox="0 0 14 12"><rect x="1" y="1" width="12" height="10" fill="none" stroke="#fff" stroke-width="1.4"/><path d="M1 1l6 5 6-5" stroke="#fff" stroke-width="1.4" fill="none"/></svg><span>Email:<br>info@briskframing.example</span></div>
    <div class="info"><svg width="14" height="14" viewBox="0 0 24 24"><path fill="#fff" d="M6.6 10.8a15 15 0 0 0 6.6 6.6l2.2-2.2a1 1 0 0 1 1-.25 11.4 11.4 0 0 0 3.6.57 1 1 0 0 1 1 1V20a1 1 0 0 1-1 1A17 17 0 0 1 3 4a1 1 0 0 1 1-1h3.5a1 1 0 0 1 1 1c0 1.25.2 2.45.57 3.57a1 1 0 0 1-.25 1z"/></svg><span>Phone:<br>+61 400 555 019</span></div>
  </div>
  <div class="col" style="left:824px">
    <h6>OUR NEWSLETTER</h6>
    <p>Sign up to stay in the Brisk Framing</p>
  </div>
  <div class="newsletter-input">Enter Email</div>
  <div class="newsletter-go"><svg width="18" height="18" viewBox="0 0 24 24"><path fill="#fff" d="M2 21l21-9L2 3v7l15 2-15 2z"/></svg></div>
  <div class="rule"></div>
  <p class="copyright">Copyright © 2022 Brisk Framing. All rights</p>
</footer>

</body>
</html>
```